Refresh Application User Interface

Pellmark wishes to update the look of its business applications. Two representative forms are shown below. Please note, we are not considering changes in functionality or usability. Our goal is a cleaner, more contemporary design.

Industry/Entity Type

Business

```html
<!DOCTYPE html>
<html lang="en">
<head>
<meta charset="utf-8">
<title>Purchase Order – Pellmark</title>
<link href="https://fonts.googleapis.com/css2?family=Lato:ital,wght@0,400;0,700;0,900;1,700&display=swap" rel="stylesheet">
<style>
:root{
  --navy:#0c3a8e;
  --green:#6cb33f;
  --green-text:#3aa22c;
  --toolbar:#3d3f45;
  --page:#ececec;
  --ink:#222;
  --muted:#555;
  --line:#9a9a9a;
  --tab-grey:#a9abae;
  --link:#1f4fa8;
  --footer:#1b1b1b;
}
*{box-sizing:border-box;margin:0;padding:0}
html,body{width:919px;height:1200px;overflow:hidden}
body{font-family:'Lato',sans-serif;color:var(--ink);background:var(--page);position:relative}
.abs{position:absolute}
.topbar{left:0;top:0;width:919px;height:28px;background:var(--navy);color:#fff;font-size:11px}
.topbar .who{left:75px;top:7px}
.topbar b{font-size:12.5px}
.topbar .links{right:75px;top:7px;word-spacing:2px}
.mainnav{left:0;top:28px;width:919px;height:60px;background:#fff;border-bottom:1px solid var(--green)}
.mainnav a{position:absolute;top:24px;font-size:13px;font-weight:700;color:var(--ink);text-decoration:none}
.mainnav .active{border:1px solid var(--green);padding:5px 7px;top:19px}
.brand{position:absolute;right:75px;top:16px;font-size:25px;font-weight:900;color:var(--navy);letter-spacing:1px}
.subnav{left:0;top:88px;width:919px;height:32px;background:#fff;border-bottom:1px solid var(--green)}
.subnav a{position:absolute;top:9px;font-size:12px;color:var(--ink);text-decoration:none}
.title{left:74px;top:180px;font-size:26px;font-weight:900}
.sectabs{left:559px;top:213px;width:284px;height:32px;background:#fff;border:1px solid var(--line);border-bottom:none;font-size:11.5px;font-weight:700}
.sectabs span{position:absolute;top:9px}
.sectabs .on{left:0;top:0;width:70px;height:32px;background:var(--toolbar);color:#fff;text-align:center;line-height:32px}
.toolbar{left:75px;top:245px;width:768px;height:35px;background:var(--toolbar);color:#fff;font-size:11px;font-weight:700}
.toolbar .tl{position:absolute;top:11px}
.toolbar .dim{color:#aaa;font-weight:700}
.panel{left:75px;top:280px;width:768px;height:802px;background:#fff}
.label{position:absolute;font-size:12px;font-weight:700;color:#333;text-align:right}
.field{position:absolute;border:1px solid var(--line);background:#fff;font-size:11px;padding:0 12px;display:flex;align-items:center;color:#333}
.select::after{content:"";position:absolute;right:0;top:0;width:34px;height:100%;border-left:1px solid var(--line)}
.chev{position:absolute;right:12px;top:50%;margin-top:-3px}
.btn{position:absolute;background:var(--green);color:#fff;font-size:11px;font-weight:700;border-radius:16px;display:flex;align-items:center;justify-content:center;letter-spacing:.5px}
.ptabs span{position:absolute;top:689px;height:29px;background:var(--tab-grey);color:#fff;font-size:11px;font-weight:700;display:flex;align-items:center;justify-content:center}
.ptabs .on{background:var(--navy)}
.pbox{left:111px;top:718px;width:699px;height:320px;border:1px solid var(--line);background:#fff}
.footer{left:0;top:1146px;width:919px;height:54px;background:var(--footer);color:#ddd;font-size:10.5px}
</style>
</head>
<body>
<div class="abs topbar">
  <div class="abs who">Logged in As <b>Dana Reyes</b> ⚙ &nbsp;&nbsp;&nbsp; Current <b>Role</b> ⌄</div>
  <div class="abs links">Touch &nbsp;| &nbsp;New Tab &nbsp;| &nbsp;Help &nbsp;| &nbsp;Support &nbsp;| &nbsp;Log Out</div>
</div>
<nav class="abs mainnav">
  <a style="left:76px">Home</a><a style="left:141px">eSource</a>
  <a class="active" style="left:211px">eBuy</a>
  <svg class="abs" style="left:226px;top:47px" width="12" height="10"><path d="M0 0h12L6 10z" fill="#6cb33f"/></svg>
  <a style="left:277px">eRequest</a><a style="left:361px">eSell</a><a style="left:419px">eStock</a><a style="left:489px">ePlan</a><a style="left:552px">Preferences</a>
  <span class="brand">PELLMARK</span>
</nav>
<nav class="abs subnav">
  <a style="left:82px;color:var(--green)">Orders</a><a style="left:150px">Receipts</a><a style="left:227px">Shipments</a><a style="left:314px">Invoices</a><a style="left:390px">Pricing</a><a style="left:458px">Tables</a><a style="left:524px">Reports</a><a style="left:598px">Inquires</a><a style="left:672px">Periodic Tasks</a><a style="left:780px">Workflows</a>
</nav>

<h1 class="abs title">PURCHASE ORDER</h1>
<div class="abs sectabs">
  <span class="on">HEADER</span>
  <span style="left:87px">LINES</span><span style="left:130px">CHARGES</span><span style="left:226px">NOTES</span>
  <svg class="abs" style="left:113px;top:4px" width="11" height="11"><circle cx="5.5" cy="5.5" r="5.5" fill="#3aa22c"/><path d="M3 5.5l2 2 3-4" stroke="#fff" stroke-width="1.5" fill="none"/></svg>
  <svg class="abs" style="left:263px;top:4px" width="11" height="11"><circle cx="5.5" cy="5.5" r="5.5" fill="#3aa22c"/><path d="M3 5.5l2 2 3-4" stroke="#fff" stroke-width="1.5" fill="none"/></svg>
</div>
<div class="abs toolbar">
  <svg class="abs" style="left:0;top:0" width="460" height="35" fill="none" stroke="#fff" stroke-width="1.5">
    <path d="M31 0v35M65 0v35M97 0v35M128 0v35M162 0v35M308 0v35M415 0v35" stroke="#555"/>
    <path d="M12 11v12a3 3 0 0 0 6 0V10a2 2 0 0 0-4 0v12"/>
    <rect x="41" y="9" width="12" height="16"/><circle cx="49" cy="19" r="3"/>
    <circle cx="76" cy="13" r="3.5" fill="#fff"/><circle cx="84" cy="19" r="3" fill="#fff"/><circle cx="76" cy="24" r="2.5" fill="#fff"/>
    <rect x="104" y="13" width="17" height="11" fill="#fff"/><path d="M109 13v-3h7v3"/>
    <circle cx="145" cy="18" r="8"/><path d="M142 15a3 3 0 1 1 3 4v2M145 23v1"/>
    <path d="M172 26l10-10M178 10l8 8M172 10l14 16"/>
    <rect x="317" y="10" width="11" height="15" fill="#fff"/>
  </svg>
  <span class="tl" style="left:191px">VIEW GL ACCOUNTS</span>
  <span class="tl" style="left:338px">POST ORDER</span>
  <span class="tl dim" style="left:464px">⌕ SEARCH</span>
  <span class="tl dim" style="left:533px">⊕ NEW</span>
  <span class="tl dim" style="left:585px">✓ APPLY</span>
  <span class="tl dim" style="left:645px">⊗ DELETE</span>
  <span class="tl dim" style="left:709px">↶ BACK</span>
</div>

<div class="abs panel"></div>
<div class="abs" style="left:138px;top:318px;font-size:15px"><b style="color:#333">Order#</b>&nbsp; 100159</div>
<div class="abs" style="left:279px;top:318px;font-size:13px;font-weight:700;color:var(--green-text)">Regular Purchase Order</div>
<div class="abs" style="left:683px;top:313px;font-size:14px;font-weight:700;color:var(--link)">Hold for Completion</div>

<span class="label" style="left:100px;top:371px;width:69px">Ship From</span>
<div class="field" style="left:204px;top:365px;width:298px;height:30px">1001</div>
<span class="label" style="left:100px;top:416px;width:69px">Address</span>
<div class="field" style="left:204px;top:410px;width:298px;height:54px;line-height:1.6;align-items:center">Harbor Clinical Co.<br>14 Birch Lane</div>
<span class="label" style="left:100px;top:491px;width:69px">City</span>
<div class="field" style="left:204px;top:485px;width:110px;height:30px">Westhaven</div>
<span class="label" style="left:330px;top:491px;width:49px">State</span>
<div class="field" style="left:391px;top:485px;width:111px;height:30px">MA</div>
<span class="label" style="left:100px;top:536px;width:69px">Zip</span>
<div class="field" style="left:204px;top:530px;width:110px;height:30px">02871-4410</div>
<span class="label" style="left:310px;top:537px;width:69px">Country</span>
<div class="field" style="left:391px;top:530px;width:111px;height:30px">02871-4410</div>
<div class="abs" style="left:207px;top:581px;font-size:12px;font-weight:700;color:#333">☑ Accept <span style="font-weight:400;color:var(--link)">(DPV Unconfirmed)</span></div>
<div class="btn" style="left:204px;top:612px;width:114px;height:31px">ADD CONTACT</div>

<div class="ptabs">
  <span style="left:111px;width:103px">ORDER INFO</span>
  <span style="left:218px;width:103px">SHIPPING</span>
  <span style="left:324px;width:103px">PAYMENTS</span>
  <span class="on" style="left:430px;width:104px">ACCOUNTS</span>
  <span style="left:537px;width:137px">TOTALS/APPROVAL</span>
</div>
<div class="abs pbox"></div>

<span class="label" style="left:120px;top:760px;width:86px">Entity</span>
<div class="field select" style="left:225px;top:755px;width:186px;height:30px">10<svg class="chev" width="10" height="6"><path d="M1 1l4 4 4-4" stroke="#666" fill="none"/></svg></div>
<span class="label" style="left:120px;top:800px;width:86px">Division</span>
<div class="field select" style="left:225px;top:794px;width:186px;height:30px">Bikes<svg class="chev" width="10" height="6"><path d="M1 1l4 4 4-4" stroke="#666" fill="none"/></svg></div>
<span class="label" style="left:120px;top:839px;width:86px">Cost Center</span>
<div class="field select" style="left:225px;top:834px;width:186px;height:30px">Admin<svg class="chev" width="10" height="6"><path d="M1 1l4 4 4-4" stroke="#666" fill="none"/></svg></div>
<span class="label" style="left:120px;top:879px;width:86px">Job Number</span>
<div class="field select" style="left:225px;top:873px;width:186px;height:30px">None<svg class="chev" width="10" height="6"><path d="M1 1l4 4 4-4" stroke="#666" fill="none"/></svg></div>

<span class="label" style="left:440px;top:760px;width:107px">Expenses Class</span>
<div class="field select" style="left:565px;top:755px;width:187px;height:30px"><svg class="chev" width="10" height="6"><path d="M1 1l4 4 4-4" stroke="#666" fill="none"/></svg></div>
<span class="label" style="left:420px;top:800px;width:64px">Allocate</span>
<div class="abs" style="left:490px;top:798px;width:20px;height:20px;border:1px solid var(--line)"></div>
<span class="label" style="left:518px;top:800px;width:30px">GL#</span>
<div class="field" style="left:565px;top:794px;width:206px;height:30px"></div>
<svg class="abs" style="left:778px;top:803px" width="13" height="13" fill="none" stroke="#888" stroke-width="1.8"><circle cx="5.5" cy="5.5" r="4"/><path d="M8.5 8.5l3.5 3.5"/></svg>
<span class="label" style="left:420px;top:839px;width:127px">Recognition Method</span>
<div class="field select" style="left:565px;top:834px;width:187px;height:30px">As Invoiced<svg class="chev" width="10" height="6"><path d="M1 1l4 4 4-4" stroke="#666" fill="none"/></svg></div>

<div class="abs" style="left:144px;top:938px;font-size:14px;font-weight:700;font-style:italic;color:#333">Click Search, or Enter Property Values and Click Apply</div>
<div class="btn" style="left:144px;top:978px;width:74px;height:31px">APPLY</div>

<footer class="abs footer">
  <div class="abs" style="left:0;width:919px;top:19px;text-align:center">Copyrights © 2018, Pellmark. All rights reserved.</div>
  <div class="abs" style="right:12px;top:19px;font-size:11px;font-weight:700;color:#fff">C17</div>
</footer>
</body>
</html>
```